Modernise Business Card

Our company has been operating for 10 years. With the start of the new decade we are looking to refresh our business card design. We manufacture a range of industrial product shipping to customers internationally. A copy of our current card, both sides, is attached. We are looking for a mature professional appearance.

```html
<!DOCTYPE html>
<html lang="en">
<head>
<meta charset="utf-8">
<title>Korvan Business Card</title>
<link rel="stylesheet" href="https://fonts.googleapis.com/css2?family=Open+Sans:wght@400;600;700;800&display=swap">
<style>
  :root {
    --navy: #053049;
    --amber: #f2a51c;
    --paper: #ffffff;
    --paper-shade: #f1f1f1;
    --ink: #0d2535;
    --stage: #262626;
  }
  * { box-sizing: border-box; margin: 0; padding: 0; }
  html, body { width: 1200px; height: 1021px; overflow: hidden; }
  body {
    background: var(--stage);
    font-family: "Open Sans", Arial, sans-serif;
    position: relative;
  }
  .card {
    position: absolute;
    left: 280px;
    width: 640px;
    height: 366px;
    overflow: hidden;
    box-shadow: 0 10px 28px rgba(0,0,0,.45);
  }
  /* Back side */
  .card--back { top: 110px; background: var(--navy); }
  .back-name {
    position: absolute;
    left: 56px; top: 118px;
    font-weight: 800;
    font-size: 92px;
    letter-spacing: 2px;
    color: var(--paper);
    line-height: 1;
  }
  .back-dot {
    position: absolute;
    left: 56px; top: 238px;
    width: 22px; height: 22px;
    background: var(--amber);
  }
  .services {
    position: absolute;
    right: 60px; bottom: 52px;
    list-style: none;
    color: var(--paper);
    font-weight: 700;
    font-size: 14px;
    line-height: 22px;
    text-transform: uppercase;
    letter-spacing: .3px;
  }
  /* Front side */
  .card--front {
    top: 516px;
    background: linear-gradient(180deg, var(--paper) 40%, var(--paper-shade) 100%);
  }
  .brand {
    position: absolute;
    left: 44px; top: 40px;
    font-weight: 800;
    font-size: 50px;
    letter-spacing: 1px;
    color: var(--navy);
    line-height: 1;
  }
  .person { position: absolute; left: 48px; top: 184px; }
  .person__name {
    font-weight: 700;
    font-size: 19px;
    color: var(--navy);
    text-transform: uppercase;
    letter-spacing: .3px;
  }
  .person__role { font-size: 14px; color: #3a4650; }
  .person__rule {
    width: 46px; height: 2px;
    background: var(--amber);
    margin-top: 18px;
  }
  .contact {
    position: absolute;
    left: 352px; top: 170px;
    font-size: 13.5px;
    color: var(--ink);
    line-height: 19px;
  }
  .contact address { font-style: normal; margin-bottom: 10px; }
  .contact ul { list-style: none; }
  .contact li { display: flex; align-items: center; gap: 8px; }
  .contact .icon { width: 13px; height: 13px; flex: none; }
  .contact .region { color: var(--navy); font-weight: 600; margin-left: 10px; }
  .contact .web-host { color: var(--amber); font-weight: 700; }
  .footer-band { position: absolute; left: 0; bottom: 0; width: 640px; height: 30px; }
</style>
</head>
<body>
  <section class="card card--back" aria-label="Card back">
    <div class="back-name">KORVAN</div>
    <div class="back-dot"></div>
    <ul class="services">
      <li>Hydraulic Adapters</li>
      <li>Hose Fittings</li>
      <li>Quick Couplings</li>
    </ul>
  </section>

  <section class="card card--front" aria-label="Card front">
    <div class="brand">KORVAN</div>

    <div class="person">
      <div class="person__name">Alan Brewer</div>
      <div class="person__role">Founder</div>
      <div class="person__rule"></div>
    </div>

    <div class="contact">
      <address>
        808-3, Lin Feng Tower<br>
        112 Harbour Road, Beilun District<br>
        Ningbo 315800 China
      </address>
      <ul>
        <li>
          <svg class="icon" viewBox="0 0 14 14"><rect x="3.5" y="1" width="7" height="12" rx="1.2" fill="none" stroke="#f2a51c" stroke-width="1.3"/><line x1="6" y1="11" x2="8" y2="11" stroke="#f2a51c" stroke-width="1.2"/></svg>
          <span>+86 139 5520 0417</span><span class="region">China</span>
        </li>
        <li>
          <svg class="icon" viewBox="0 0 14 14"><rect x="3.5" y="1" width="7" height="12" rx="1.2" fill="none" stroke="#f2a51c" stroke-width="1.3"/><line x1="6" y1="11" x2="8" y2="11" stroke="#f2a51c" stroke-width="1.2"/></svg>
          <span>+61 412 708 335</span><span class="region">Australia</span>
        </li>
        <li>
          <svg class="icon" viewBox="0 0 14 14"><rect x="1" y="3" width="12" height="8.5" fill="none" stroke="#f2a51c" stroke-width="1.3"/><polyline points="1,3 7,8 13,3" fill="none" stroke="#f2a51c" stroke-width="1.3"/></svg>
          <span>abrewer@korvanfittings.com</span>
        </li>
        <li>
          <svg class="icon" viewBox="0 0 14 14"><circle cx="7" cy="7" r="5.7" fill="none" stroke="#f2a51c" stroke-width="1.2"/><ellipse cx="7" cy="7" rx="2.5" ry="5.7" fill="none" stroke="#f2a51c" stroke-width="1"/><line x1="1.3" y1="7" x2="12.7" y2="7" stroke="#f2a51c" stroke-width="1"/></svg>
          <span>www.<span class="web-host">korvanfittings</span>.com</span>
        </li>
      </ul>
    </div>

    <svg class="footer-band" viewBox="0 0 640 30" preserveAspectRatio="none" aria-hidden="true">
      <polygon points="0,0 345,0 333,30 0,30" fill="#053049"/>
      <polygon points="351,0 640,0 640,30 339,30" fill="#f2a51c"/>
    </svg>
  </section>
</body>
</html>
```